Post Card Mailer Design-

Marbrook Elder Living is a subsidiary of the Marbrook Haven Group. This Post Card is specifically for the Marbrook Elder Living company and brand. Create a 4 x 6, front and back, Post Card. This Post Card will be an invitation to prospective clients and/or caring family members to join us for informative and personalized get together(s) to discuss the Senior Care Home that we are opening. It is a modern and state of the art home. Like the home, the Post Card must be eye catching, unique in its deliverables (as it doesn’t feel like a care facility) and demonstrate both attention to detail and comfort. Our organization is sophisticated and built around warmth, care and individualized personal attention. The most important aspect of this design is to focus on creating a nurturing, warm, and inviting feel that would attract a prospective client to want to join us for an educational event.

I am open to the creativity of the designer to develop something based on the above criteria; however I would like the design to work well with our existing collateral material. What I mean by that is that while I want everything to have its own personality and stand out as its own brand representative, I still need to be able to tell that the overall design concept stays stylistically inside of the same ‘family’ of existing designed material. Because of this, I would like for the designer to pull inspiration from the link to our website (Located below) as well as from our recently refreshed business cards (Attached Below). This should allow the Post Card design to be unique and creative, while still staying inside of a framework and the feel/style that I am looking for.

Finally, I want all the designers to understand that this Post Card design is for an educational and informative, small sized event where we are looking to attract attendance from prospective clients and/or caring family members of active, positive, and happy seniors/elders. We are responsible for providing personalized care for a culturally and ethnically diverse make-up of active, positive, and happy seniors/elders. The photos that are used must be tasteful, graceful, and elegant.
Updates

Industry/Entity Type

It Company

Requirements
Must have
• • The company logo must be included.•
• Look under the Marbrook Elder Living tab at www.marbrookhavengroup.net.

```html
<!DOCTYPE html>
<html lang="en">
<head>
<meta charset="utf-8">
<title>Marbrook Elder Living – Postcard Mailer</title>
<link rel="stylesheet" href="https://fonts.googleapis.com/css2?family=Russo+One&family=Roboto:wght@400;500&display=swap">
<style>
  :root {
    --stage: #2b2b2b;
    --teal: #8dbfca;
    --slate: #555557;
    --slate-dark: #444446;
    --frame: #d9d9dc;
    --paper: #ffffff;
    --navy: #1b2a6b;
    --ink: #111111;
    --address: #3a4150;
    --photo-bed: #a88a5f;
    --photo-living: #8a6a4e;
    --photo-kitchen: #7a3b28;
  }
  html, body { margin: 0; padding: 0; overflow: hidden; }
  body {
    width: 900px; height: 1200px; position: relative;
    background: var(--stage);
    font-family: "Roboto", Arial, sans-serif;
  }
  .card { position: absolute; overflow: hidden; box-shadow: 0 4px 14px rgba(0,0,0,.5); }
  .card svg.shapes { position: absolute; inset: 0; }
  .card-front { left: 172px; top: 60px; width: 558px; height: 575px; background: var(--frame); }
  .card-back { left: 60px; top: 723px; width: 782px; height: 417px; background: var(--frame); }
  .abs { position: absolute; }

  .event-day {
    left: 40px; top: 38px; font-family: "Russo One", sans-serif;
    font-size: 86px; line-height: 1; color: var(--ink); letter-spacing: 2px;
  }
  .event-month { left: 38px; top: 120px; font-size: 29px; color: var(--ink); letter-spacing: 1px; }
  .join-us {
    left: 16px; top: 184px; font-family: "Russo One", sans-serif; font-size: 44px;
    color: #9aa9b8; transform: skewX(-14deg); letter-spacing: 1px;
  }
  .brand-box {
    background: var(--paper); display: flex; align-items: center; justify-content: center;
    text-align: center;
  }
  .brand-name { color: #5a9eaa; font-weight: 400; line-height: 1.15; }
  .front-brand { left: 219px; top: 267px; width: 126px; height: 83px; }
  .front-brand .brand-name { font-size: 17px; }
  .contact { line-height: 1.28; text-align: right; }
  .contact b { font-weight: 500; }
  .front-contact { left: 160px; top: 357px; width: 230px; color: var(--paper); font-size: 15px; }
  .front-contact b { color: var(--navy); }
  .front-contact .small { font-size: 13px; }
  .address {
    font-family: "Russo One", sans-serif; white-space: nowrap; letter-spacing: .5px;
  }
  .front-address { left: 0; width: 558px; top: 553px; text-align: center; font-size: 13.5px; color: var(--address); }

  .back-brand { left: 108px; top: 113px; width: 162px; height: 110px; }
  .back-brand .brand-name { font-size: 22px; }
  .back-contact { left: 40px; top: 282px; width: 280px; color: var(--paper); font-size: 16px; }
  .back-contact b { color: var(--teal); }
  .back-rule { left: 28px; top: 375px; width: 332px; height: 1px; background: #9a9a9c; }
  .back-address { left: 22px; top: 380px; font-size: 13px; color: var(--paper); }
</style>
</head>
<body>

<section class="card card-front" aria-label="Postcard front">
  <svg class="shapes" width="558" height="575" viewBox="0 0 558 575">
    <polygon points="0,27 318,27 275,155 0,155" fill="var(--teal)"/>
    <polygon points="0,163 270,163 248,240 0,240" fill="var(--slate)"/>
    <polygon points="320,27 558,27 558,248 262,248" fill="var(--photo-bed)" role="img" aria-label="Photo of a bright, furnished bedroom"/>
    <polygon points="0,260 558,260 558,268 320,552 300,552 0,262" fill="var(--teal)"/>
    <polygon points="0,275 40,318 0,340" fill="var(--slate)"/>
    <polygon points="0,330 40,318 290,552 0,552" fill="var(--photo-living)" role="img" aria-label="Photo of a living room with leather sectional sofa"/>
    <polygon points="495,325 558,270 558,385" fill="var(--slate)"/>
    <polygon points="330,552 492,360 558,395 558,552" fill="var(--photo-kitchen)" role="img" aria-label="Photo of a modern kitchen with wood cabinets"/>
  </svg>
  <div class="abs event-day">25</div>
  <div class="abs event-month">may, 2014</div>
  <div class="abs join-us">Join us!</div>
  <div class="abs brand-box front-brand"><span class="brand-name">Marbrook<br>Elder Living</span></div>
  <div class="abs contact front-contact">
    <div><b>Phone :</b> (808) 555-0186</div>
    <div><b>Fax :</b> (808) 555-0122</div>
    <div class="small"><b>E-mail :</b> hana@marbrookcare.com</div>
    <div class="small"><b>Web :</b> www.marbrookcare.com</div>
  </div>
  <div class="abs address front-address">1480 Lanakila Ave., Suite 210, Honolulu, HI 96817</div>
</section>

<section class="card card-back" aria-label="Postcard back">
  <svg class="shapes" width="782" height="417" viewBox="0 0 782 417">
    <polygon points="0,0 462,0 372,245 0,245" fill="var(--teal)"/>
    <polygon points="462,0 478,0 388,245 372,245" fill="var(--paper)"/>
    <rect x="0" y="245" width="372" height="8" fill="#bfbfc2"/>
    <polygon points="0,262 360,262 405,417 0,417" fill="var(--slate)"/>
    <polygon points="360,262 380,262 405,417 385,417" fill="var(--slate-dark)"/>
  </svg>
  <div class="abs brand-box back-brand"><span class="brand-name">Marbrook<br>Elder Living</span></div>
  <div class="abs contact back-contact">
    <div><b>Phone :</b> (808) 555-0186</div>
    <div><b>Fax :</b> (808) 555-0122</div>
    <div><b>E-mail :</b> hana@marbrookcare.com</div>
    <div><b>Web :</b> www.marbrookcare.com</div>
  </div>
  <div class="abs back-rule"></div>
  <div class="abs address back-address">1480 Lanakila Ave., Suite 210, Honolulu, HI 96817</div>
</section>

</body>
</html>
```